Alcohol designs Birthday Sign's needs more templates

We are after 10 new designs for signable custom birthday signs, alcohol theme inspired (beer, wine, spirits) for this batch, You do not need to provide 10 designs however the winner will be based on final look and quantity.
For example someone may win with one design or ten designs. We will also look at purchasing more individual designs for any winners or potential winners. Designs must be in layers, CMYK, 8bits channel, saved as TIFF or PDS or AI, size is 460mm wide x by 1060mm high with 30mm bleed included, total graphic size will be 430 x 1030 at 300ppi, any text must be editable and font files included. see attached for sample's, signable area needs to be on each design and a sample persons name, other then that we a excited to see what everyone comes up with
Updates
Reason: Allow more designs to be supplied form current designers and new designers. Also to allow us to choose more than one designer by adding a second/third place
Target Market(s)
Birthday
Requirements
Must have
- Layers.
- Space for people to sign
Nice to have
- At least 3 designs (These can be of the same template you design just with a small them change beer, wine etc)

```html
<!DOCTYPE html>
<html lang="en">
<head>
<meta charset="utf-8">
<title>Beer Birthday Sign</title>
<link href="https://fonts.googleapis.com/css2?family=Oswald:wght@400;500;700&display=swap" rel="stylesheet">
<style>
  :root {
    --backdrop: #e9e6e1;
    --sign-red: #d3222b;
    --sign-red-deep: #b81a22;
    --signing-red: #c81e27;
    --edge-cream: #f3ead8;
    --beer-orange: #f5a642;
    --beer-orange-light: #fbc56a;
    --shadow-brown: #3b1a12;
    --rule-dark: #4a1510;
    --ribbon-black: #1c1816;
  }
  * { margin: 0; padding: 0; box-sizing: border-box; }
  html, body {
    width: 1200px;
    height: 1099px;
    overflow: hidden;
    background: var(--backdrop);
  }
  .sign {
    position: absolute;
    left: 375px;
    top: 31px;
    width: 450px;
    height: 1036px;
    background: radial-gradient(ellipse at 50% 40%, var(--sign-red) 55%, var(--sign-red-deep) 100%);
    border-left: 10px solid var(--edge-cream);
    border-right: 10px solid var(--edge-cream);
    font-family: "Oswald", "Arial Narrow", sans-serif;
    box-shadow: 0 6px 18px rgba(0,0,0,0.25);
  }
  .hero-art {
    position: absolute;
    left: 10px;
    right: 10px;
    top: 130px;
    height: 200px;
    background: radial-gradient(ellipse at 50% 45%, var(--beer-orange-light) 0%, var(--beer-orange) 40%, rgba(245,166,66,0) 72%);
  }
  .headline {
    position: absolute;
    left: 0;
    right: 0;
    top: 352px;
    text-align: center;
    line-height: 0.98;
  }
  .headline span {
    display: block;
    font-weight: 700;
    font-size: 46px;
    letter-spacing: -1px;
    color: var(--beer-orange);
    text-shadow: 3px 3px 0 var(--shadow-brown), 4px 4px 0 var(--shadow-brown);
  }
  .headline .line-one { margin-right: 40px; }
  .headline .line-two { margin-left: 40px; }
  .date-strip {
    position: absolute;
    left: 30px;
    right: 30px;
    top: 452px;
    height: 58px;
    border-top: 4px solid var(--rule-dark);
    border-bottom: 4px solid var(--rule-dark);
    text-align: center;
    font-weight: 500;
    font-size: 38px;
    line-height: 50px;
    color: var(--beer-orange);
    letter-spacing: 1px;
  }
  .signing-area {
    position: absolute;
    left: 22px;
    right: 22px;
    top: 540px;
    height: 245px;
    background: var(--signing-red);
  }
  .greeting {
    position: absolute;
    left: 0;
    right: 0;
    top: 788px;
    text-align: center;
    font-weight: 700;
    font-size: 42px;
    letter-spacing: -1px;
    color: var(--beer-orange);
    text-shadow: 3px 3px 0 var(--shadow-brown);
  }
  .name-ribbon {
    position: absolute;
    left: 20px;
    top: 848px;
    width: 410px;
    height: 100px;
  }
  .name-ribbon .name {
    font-family: "Oswald", "Arial Narrow", sans-serif;
    font-weight: 700;
    font-size: 46px;
    fill: var(--beer-orange);
  }
</style>
</head>
<body>
  <main class="sign">
    <div class="hero-art" role="img" aria-label="Illustration of two hands clinking foaming beer mugs"></div>

    <h1 class="headline">
      <span class="line-one">CUSTOM TEXT</span>
      <span class="line-two">CUSTOM TEXT</span>
    </h1>

    <p class="date-strip">01.08.2017</p>

    <div class="signing-area" aria-label="Space for guest signatures"></div>

    <p class="greeting">HAPPY BIRTHDAY</p>

    <svg class="name-ribbon" viewBox="0 0 410 100" aria-label="Name banner">
      <polygon points="0,22 410,0 392,42 410,78 0,100 18,60" fill="var(--ribbon-black)"/>
      <text class="name" x="205" y="68" text-anchor="middle" transform="rotate(-3 205 55)">BEER</text>
    </svg>
  </main>
</body>
</html>
```